Commercial Real Estate

We need a business card design for a new commercial real estate business that specializes in apartment building brokerage. Not individual units but the entire complex. We find and represent the owners existing buildings and well as new buyers for those buildings. The design should convey trust, integrity, knowledge and growth. It should be easily read.

Target Market(s)

40 to 65 years old

Industry/Entity Type

Real Estate

```html
<!DOCTYPE html>
<html lang="en">
<head>
<meta charset="utf-8">
<title>Crestline Property Investments – Business Card</title>
<link rel="stylesheet" href="https://fonts.googleapis.com/css2?family=Open+Sans:wght@400;600;700&display=swap">
<style>
  :root {
    --backdrop: #e9e6e2;
    --card: #ffffff;
    --card-edge: #dcdcdc;
    --ink: #3d4a4f;
    --name-grey: #7f8c8f;
    --muted: #6b7375;
    --teal: #4fb3b5;
    --teal-deep: #2f8f92;
  }
  * { box-sizing: border-box; margin: 0; padding: 0; }
  html, body { width: 1200px; height: 913px; overflow: hidden; }
  body {
    background: var(--backdrop);
    font-family: "Open Sans", Arial, sans-serif;
    color: var(--ink);
    position: relative;
  }
  .card {
    position: absolute;
    top: 308px;
    width: 520px;
    height: 297px;
    background: var(--card);
    border: 1px solid var(--card-edge);
    box-shadow: 0 6px 18px rgba(0,0,0,0.12);
  }
  .card--front { left: 50px; }
  .card--back { left: 630px; }

  .brand {
    position: absolute;
    display: flex;
    flex-direction: column;
    align-items: center;
    gap: 6px;
  }
  .brand__row { display: flex; align-items: center; gap: 10px; }
  .brand__square { width: 14px; height: 14px; background: var(--teal); }
  .brand__name,
  .brand__tagline {
    color: var(--ink);
    font-weight: 700;
    letter-spacing: 1px;
  }
  .brand__name { font-size: 30px; text-transform: uppercase; letter-spacing: 3px; }
  .brand__tagline { font-size: 13px; }
  .brand__rule { width: 100%; height: 2px; background: var(--teal); }

  .card--front .brand { left: 0; right: 0; top: 112px; }
  .card--back .brand { left: 26px; top: 128px; }
  .card--back .brand__name { font-size: 24px; letter-spacing: 2px; }
  .card--back .brand__tagline { font-size: 11px; }

  .contact {
    position: absolute;
    left: 300px;
    top: 64px;
    width: 200px;
  }
  .contact__name { font-size: 17px; font-weight: 700; color: var(--name-grey); line-height: 1.1; }
  .contact__role { font-size: 10px; color: var(--muted); margin-bottom: 8px; }
  .contact__list { list-style: none; }
  .contact__item {
    display: flex;
    align-items: flex-start;
    gap: 10px;
    font-size: 11.5px;
    line-height: 1.35;
    color: var(--ink);
    margin-bottom: 3px;
  }
  .contact__icon { width: 11px; height: 11px; flex: none; margin-top: 3px; fill: var(--muted); }
  .contact__item--web { color: var(--teal-deep); }
</style>
</head>
<body>
  <section class="card card--front" aria-label="Card front">
    <div class="brand">
      <div class="brand__row">
        <span class="brand__square"></span>
        <span class="brand__name">Crestline</span>
      </div>
      <span class="brand__rule"></span>
      <span class="brand__tagline">Property Investments</span>
    </div>
  </section>

  <section class="card card--back" aria-label="Card back">
    <div class="brand">
      <div class="brand__row">
        <span class="brand__square"></span>
        <span class="brand__name">Crestline</span>
      </div>
      <span class="brand__rule"></span>
      <span class="brand__tagline">Property Investments</span>
    </div>

    <div class="contact">
      <p class="contact__name">Your Name</p>
      <p class="contact__role">Director</p>
      <ul class="contact__list">
        <li class="contact__item">
          <svg class="contact__icon" viewBox="0 0 12 12" aria-hidden="true"><path d="M6 0a4 4 0 0 0-4 4c0 3 4 8 4 8s4-5 4-8a4 4 0 0 0-4-4zm0 5.5A1.5 1.5 0 1 1 6 2.5a1.5 1.5 0 0 1 0 3z"/></svg>
          <span>Your commercial address<br>in just two line</span>
        </li>
        <li class="contact__item">
          <svg class="contact__icon" viewBox="0 0 12 12" aria-hidden="true"><path d="M1 3c0-1 1-2 5-2s5 1 5 2v1H8.5V3h-5v1H1zM2.5 5h7l1 6h-9z"/></svg>
          <span>00000000000</span>
        </li>
        <li class="contact__item">
          <svg class="contact__icon" viewBox="0 0 12 12" aria-hidden="true"><path d="M0 2h12v8H0zm1 1v.3l5 3.2 5-3.2V3z"/></svg>
          <span>yourname@website.com</span>
        </li>
        <li class="contact__item contact__item--web">
          <svg class="contact__icon" viewBox="0 0 12 12" aria-hidden="true"><circle cx="6" cy="6" r="5.5"/><path d="M0.5 6h11M6 0.5v11" stroke="#fff" stroke-width="0.8"/></svg>
          <span>www.website.com</span>
        </li>
      </ul>
    </div>
  </section>
</body>
</html>
```